Business Card Design Project

We need a business card design for a company based in San Francisco called PlanGlide. PlanGlide makes customized academic planners for high schools and middle schools. Currently we sell directly to the schools who either re-sell or give the planners to their students. The planners are designed to help students stay organized and manage their time. The books are unique in that they are made individually for each school and include the school's events, student artwork and most importantly the daily class schedule in each week. This helps the student to understand what classes they have each day and what homework they need to do each night.

Currently the product is B:B; however, we are exploring ways in which to make this a B:C. Please review website at www.planglide.net

The final design should communicate time management and organization.

Card should be one-sided

Information for the business card should include

Dorothy Kellner Voss
Founder
dorothy@planglide.net
415-836-1752

Target Market(s)

High school and middle school administrators

Industry/Entity Type

School

Requirements
Must have
• One sided design
Nice to have
• I'm open to new interpretations of the logo as well as color usage. I'm also open to changing the font of the logo type.
Should not have
• Please use a san serif font.

```html
<!DOCTYPE html>
<html lang="en">
<head>
<meta charset="utf-8">
<title>Dorothy Kellner Voss — PlanGlide</title>
<link rel="stylesheet" href="https://fonts.googleapis.com/css2?family=Mulish:ital,wght@0,400;0,500;1,400&display=swap">
<style>
  :root {
    --card-white: #ffffff;
    --brand-red: #dc1f3f;
    --ink: #231f20;
  }
  * { margin: 0; padding: 0; box-sizing: border-box; }
  html, body {
    width: 1200px;
    height: 686px;
    overflow: hidden;
    background: var(--card-white);
  }
  .business-card {
    position: relative;
    width: 1200px;
    height: 686px;
    background: var(--card-white);
    font-family: "Mulish", sans-serif;
    color: var(--ink);
  }
  .dot-border {
    position: absolute;
    top: 28px;
    left: 0;
    width: 1200px;
    height: 24px;
  }
  .identity {
    position: absolute;
    top: 66px;
    right: 32px;
    text-align: right;
  }
  .person-name {
    font-size: 84px;
    font-weight: 500;
    line-height: 1;
    letter-spacing: -0.5px;
    color: var(--brand-red);
  }
  .person-title {
    margin-right: 5px;
    font-size: 42px;
    font-style: italic;
    font-weight: 400;
    line-height: 1.05;
    color: var(--ink);
  }
  .brand-mark {
    position: absolute;
    top: 300px;
    right: 36px;
    display: flex;
    align-items: center;
    gap: 18px;
  }
  .brand-dot {
    width: 34px;
    height: 34px;
    border-radius: 50%;
    background: var(--brand-red);
    flex-shrink: 0;
  }
  .brand-name {
    font-size: 62px;
    font-weight: 500;
    line-height: 1;
    letter-spacing: -0.5px;
    color: var(--brand-red);
  }
  .contact-list {
    position: absolute;
    left: 18px;
    top: 476px;
    list-style: none;
  }
  .contact-item {
    display: flex;
    align-items: center;
    height: 69px;
    margin-bottom: 21px;
  }
  .contact-badge {
    width: 69px;
    height: 69px;
    border-radius: 50%;
    background: var(--brand-red);
    color: var(--ink);
    display: flex;
    align-items: center;
    justify-content: center;
    font-size: 52px;
    line-height: 1;
    padding-bottom: 8px;
    flex-shrink: 0;
  }
  .contact-value {
    margin-left: 22px;
    font-size: 48px;
    font-weight: 400;
    color: var(--ink);
  }
</style>
</head>
<body>
  <div class="business-card">
    <svg class="dot-border" viewBox="0 0 1200 24" aria-hidden="true">
      <defs>
        <pattern id="dot-row" x="5.5" y="0" width="35.4" height="24" patternUnits="userSpaceOnUse">
          <circle cx="12" cy="12" r="12" fill="#231f20"/>
        </pattern>
      </defs>
      <rect x="5" y="0" width="1193" height="24" fill="url(#dot-row)"/>
    </svg>

    <header class="identity">
      <h1 class="person-name">Dorothy Kellner Voss</h1>
      <p class="person-title">Founder</p>
    </header>

    <div class="brand-mark">
      <span class="brand-dot" aria-hidden="true"></span>
      <span class="brand-name">PlanGlide</span>
    </div>

    <ul class="contact-list">
      <li class="contact-item">
        <span class="contact-badge">p</span>
        <span class="contact-value">415-836-1752</span>
      </li>
      <li class="contact-item">
        <span class="contact-badge">e</span>
        <span class="contact-value">dorothy@planglide.net</span>
      </li>
    </ul>
  </div>
</body>
</html>
```